Commercial Real Estate website

Need a web design commercial real estate company specializing in retail shopping centers based in Orlando, FL. We would like pictures of Orlando city skyline with hues and colors that go with hot pink. We want to stress the relationship of time on the value of real estate.
It should gave a rotating page that highlights our property listings.

Target Market(s)

Owners of shopping centers and national retail tenants looking for tenant representatives.

Industry/Entity Type

Real Estate

Number of Pages Required

5+ page

Font styles to use
Serif

Colors
e34197

Requirements
Must have
• Pictures of commercial retail grocery anchored shopping centers and city scapes and skylines.

```html
<!DOCTYPE html>
<html lang="en">
<head>
<meta charset="utf-8">
<title>Hourmark Commercial</title>
<link href="https://fonts.googleapis.com/css2?family=Open+Sans:wght@400;600;700;800&display=swap" rel="stylesheet">
<style>
:root{
  --pink:#e34197;
  --pink-dark:#c92f80;
  --ink:#333;
  --muted:#888;
  --dark-btn:#3b3b3b;
  --light:#f3f3f3;
  --line:#e2e2e2;
  --bottom:#2b2b2b;
  --white:#fff;
}
*{box-sizing:border-box;margin:0;padding:0}
html,body{width:1200px;height:2252px;overflow:hidden}
body{font-family:"Open Sans",Arial,sans-serif;color:var(--ink);background:var(--white);position:relative}
.btn{display:inline-block;background:var(--dark-btn);color:var(--white);font-size:11px;font-weight:700;letter-spacing:.5px;padding:8px 16px;text-transform:uppercase}
.site-header{height:112px;display:flex;align-items:center;justify-content:space-between;padding:0 64px 0 60px}
.brand{display:flex;align-items:center;gap:10px}
.brand-mark{width:14px;height:14px;background:var(--pink)}
.brand-name{font-size:24px;font-weight:700;color:var(--ink);line-height:1}
.main-nav{display:flex;gap:6px}
.main-nav a{font-size:12px;font-weight:600;color:#666;padding:7px 12px;text-transform:uppercase;border:1px solid transparent}
.main-nav a.active{border-color:#bbb;color:var(--ink)}
.hero{position:absolute;top:112px;left:0;width:1200px;height:480px;background:linear-gradient(180deg,#6a6aa8 0%,#8a6e9c 35%,#3a3e66 60%,#1d2647 100%)}
.hero-text{position:absolute;top:232px;left:0;width:100%;text-align:center;color:var(--white)}
.hero-text h1{font-size:44px;font-weight:800;letter-spacing:1px}
.hero-text p{font-size:13px;line-height:20px;margin-top:6px;opacity:.9}
.hero-arrow{position:absolute;top:238px;width:24px;height:40px}
.features{position:absolute;top:592px;left:0;width:1200px;height:336px;background:var(--pink)}
.feature{position:absolute;top:0;width:300px;text-align:center;color:var(--white)}
.feature .icon{width:66px;height:66px;border-radius:50%;background:#5a5a5a;border:4px solid var(--white);margin:34px auto 0;display:flex;align-items:center;justify-content:center}
.feature h3{font-size:15px;font-weight:700;margin-top:16px;text-transform:uppercase}
.feature p{font-size:11px;line-height:17px;margin:8px auto 16px;width:240px}
.feature.commercial{left:98px}
.feature.retail{left:770px}
.feature.residential{left:452px;width:308px;height:336px;background:var(--white);color:var(--ink);top:-40px;height:376px;box-shadow:0 2px 8px rgba(0,0,0,.15)}
.feature.residential .photo{height:128px;margin:10px;background:linear-gradient(180deg,#cfe0ef,#8ea8be)}
.feature.residential .icon{margin:-34px auto 0;position:relative}
.feature.residential p{color:#777}
.listings{position:absolute;top:960px;left:0;width:1200px;text-align:center}
.section-title{font-size:24px;font-weight:700;letter-spacing:.5px;text-transform:uppercase}
.section-title em{font-style:normal;color:var(--pink)}
.title-rule{width:70px;height:2px;background:var(--pink);margin:10px auto 0}
.cards{display:flex;gap:32px;justify-content:center;margin-top:44px}
.card{width:228px;text-align:left;background:#fafafa;border:1px solid var(--line);padding:0 0 14px}
.card .photo{height:150px}
.card h4{font-size:10px;font-weight:700;margin:12px 12px 0;text-transform:uppercase}
.card .price{font-size:17px;color:var(--pink);font-weight:600;margin:6px 12px}
.card p{font-size:10px;line-height:15px;color:var(--muted);margin:0 12px 10px}
.card .btn{margin-left:12px;padding:6px 12px;font-size:10px}
.dots{display:flex;gap:6px;justify-content:center;margin-top:38px}
.dots span{width:8px;height:8px;border-radius:50%;background:#555}
.dots span.on{background:var(--pink)}
.about{position:absolute;top:1532px;left:0;width:1200px;height:408px;background:var(--light)}
.about .person{position:absolute;left:40px;top:20px;width:300px;height:388px;background:linear-gradient(180deg,#dde3ea,#b9c7d6)}
.about-text{position:absolute;left:352px;top:44px;width:400px}
.about-text .pre{font-size:20px;font-weight:600;color:#555}
.about-text h2{font-size:28px;font-weight:800;line-height:32px;text-transform:uppercase}
.about-text p{font-size:11px;line-height:17px;color:#777;margin-top:14px}
.about-text .btn{margin-top:22px}
.contact-form{position:absolute;left:806px;top:36px;width:300px}
.contact-form h3{font-size:20px;font-weight:700;color:#555;text-transform:uppercase;margin-bottom:16px}
.contact-form .field{height:40px;background:var(--white);border:1px solid var(--line);margin-bottom:10px;font-size:10px;color:#999;padding:12px}
.contact-form .submit{display:inline-block;background:var(--pink);color:var(--white);font-size:11px;font-weight:700;padding:9px 14px;text-transform:uppercase}
.site-footer{position:absolute;top:1940px;left:0;width:1200px;height:260px;background:var(--pink);color:var(--white);display:flex;padding:28px 60px 0 60px;gap:40px}
.site-footer .col{width:240px}
.site-footer h5{font-size:12px;font-weight:700;text-transform:uppercase;margin-bottom:14px}
.site-footer p,.site-footer li{font-size:11px;line-height:20px}
.site-footer ul{list-style:none}
.site-footer li::before{content:"›";margin-right:8px}
.signup-input{margin-top:12px;height:28px;width:200px;border:1px solid rgba(255,255,255,.7);font-size:10px;padding:6px 8px}
.signup-btn{display:inline-block;margin-top:8px;background:var(--dark-btn);font-size:10px;font-weight:700;padding:6px 14px}
.contact-line{display:flex;gap:10px;align-items:flex-start;margin-bottom:6px}
.contact-line svg{flex:none;margin-top:4px}
.bottom-bar{position:absolute;top:2200px;left:0;width:1200px;height:52px;background:var(--bottom);color:#bbb;font-size:10px;display:flex;align-items:center;justify-content:space-between;padding:0 60px}
</style>
</head>
<body>
<header class="site-header">
  <div class="brand"><span class="brand-mark"></span><span class="brand-name">Hourmark</span></div>
  <nav class="main-nav">
    <a class="active">Home</a><a>About Us</a><a>Property Listings</a><a>Services</a><a>News</a><a>Contact Us</a>
  </nav>
</header>

<section class="hero" role="img" aria-label="Orlando city skyline at dusk reflected on the lake">
  <svg class="hero-arrow" style="left:8px" viewBox="0 0 24 40"><path d="M16 12l-8 8 8 8" stroke="#fff" stroke-width="3" fill="none"/></svg>
  <svg class="hero-arrow" style="right:8px" viewBox="0 0 24 40"><path d="M8 12l8 8-8 8" stroke="#fff" stroke-width="3" fill="none"/></svg>
  <div class="hero-text">
    <h1>HOURMARK COMMERCIAL</h1>
    <p>Time shapes the value of every property we represent across Central Florida.<br>Retail centers, offices and land matched with the right tenants and owners.</p>
  </div>
</section>

<section class="features">
  <div class="feature commercial">
    <div class="icon"><svg width="24" height="32" viewBox="0 0 24 32"><rect x="2" y="2" width="20" height="28" rx="3" fill="none" stroke="#fff" stroke-width="2.5"/><rect x="6" y="6" width="12" height="16" fill="#fff"/></svg></div>
    <h3>Commercial</h3>
    <p>Office and mixed use space for growing firms, leased and sold with clear terms and fast timelines.</p>
    <span class="btn">Read More</span>
  </div>
  <div class="feature residential">
    <div class="photo" role="img" aria-label="Photo of a modern residential tower"></div>
    <div class="icon"><svg width="32" height="28" viewBox="0 0 32 28"><path d="M4 14L16 3l12 11M8 11v14h16V11" fill="none" stroke="#fff" stroke-width="2.5"/><rect x="13" y="17" width="6" height="8" fill="#fff"/></svg></div>
    <h3>Residential</h3>
    <p>Multifamily and residential assets priced on solid data, with a team that watches the market daily.</p>
    <span class="btn">Read More</span>
  </div>
  <div class="feature retail">
    <div class="icon"><svg width="32" height="28" viewBox="0 0 32 28"><path d="M2 3h5l4 15h15l3-11H9" fill="none" stroke="#fff" stroke-width="2.5"/><circle cx="13" cy="24" r="2.5" fill="#fff"/><circle cx="24" cy="24" r="2.5" fill="#fff"/></svg></div>
    <h3>Retail Shopping</h3>
    <p>Grocery anchored shopping centers and national tenant representation throughout Orlando.</p>
    <span class="btn">Read More</span>
  </div>
</section>

<section class="listings">
  <h2 class="section-title">Our <em>Property</em> Listings</h2>
  <div class="title-rule"></div>
  <div class="cards">
    <article class="card"><div class="photo" role="img" aria-label="Photo of city towers" style="background:linear-gradient(180deg,#9fc3e6,#5f7f9e)"></div><h4>Lake Eola Retail Center</h4><div class="price">$ 110,000</div><p>Anchored center with strong traffic and long term national tenants in place.</p><span class="btn">Read More</span></article>
    <article class="card"><div class="photo" role="img" aria-label="Photo of glass office buildings" style="background:linear-gradient(180deg,#b7d3ec,#6f8ea9)"></div><h4>Colonial Plaza Offices</h4><div class="price">$ 110,000</div><p>Modern office floors close to downtown with parking and easy highway access.</p><span class="btn">Read More</span></article>
    <article class="card"><div class="photo" role="img" aria-label="Photo of downtown skyline" style="background:linear-gradient(180deg,#7fb0e0,#4b6d8f)"></div><h4>Orange Avenue Tower</h4><div class="price">$ 110,000</div><p>High rise suites with skyline views, flexible layouts and on site amenities.</p><span class="btn">Read More</span></article>
    <article class="card"><div class="photo" role="img" aria-label="Photo of skyscrapers" style="background:linear-gradient(180deg,#a8cdee,#58789a)"></div><h4>Winter Park Commons</h4><div class="price">$ 110,000</div><p>Neighborhood shopping center with grocery anchor and room for new pads.</p><span class="btn">Read More</span></article>
  </div>
  <div class="dots"><span class="on"></span><span></span><span></span></div>
</section>

<section class="about">
  <div class="person" role="img" aria-label="Photo of a company broker in a shirt and tie"></div>
  <div class="about-text">
    <div class="pre">Welcome to</div>
    <h2>Hourmark Commercial</h2>
    <p>We help owners of shopping centers and national retail tenants make the right move at the right time. Our brokers track every shift in the Orlando market so your property is priced and leased for its true value.</p>
    <p>From site selection to lease renewal, we work with care and speed, keeping each client informed at every step of the deal.</p>
    <span class="btn">Read More ›</span>
  </div>
  <form class="contact-form">
    <h3>Get In Touch</h3>
    <div class="field">Your Name</div>
    <div class="field">E-mail</div>
    <div class="field">Website</div>
    <div class="field">Subject</div>
    <div class="field">Comment</div>
    <span class="submit">Submit Enquiry</span>
  </form>
</section>

<footer class="site-footer">
  <div class="col">
    <h5>Sign Up To Receive Email</h5>
    <p>Get new listings and market updates sent straight to your inbox.</p>
    <div class="signup-input">Enter Name</div>
    <div class="signup-input" style="margin-top:8px">Enter Email</div>
    <span class="signup-btn">Subscribe</span>
  </div>
  <div class="col">
    <h5>Featured Services</h5>
    <ul><li>Residential</li><li>Commercial</li><li>Retail Shopping</li><li>Leasing</li></ul>
  </div>
  <div class="col">
    <h5>Quick Links</h5>
    <ul><li>Support</li><li>Get in touch</li><li>About us</li><li>Terms of use</li></ul>
  </div>
  <div class="col">
    <h5>Contact Us</h5>
    <div class="contact-line"><svg width="10" height="14" viewBox="0 0 10 14"><path d="M5 0a5 5 0 015 5c0 4-5 9-5 9S0 9 0 5a5 5 0 015-5z" fill="#fff"/></svg><p>Hourmark Commercial<br>P.O. Box 000, Orlando, FL</p></div>
    <div class="contact-line"><svg width="12" height="12" viewBox="0 0 12 12"><path d="M2 0l3 3-1.5 1.5a7 7 0 004 4L9 7l3 3-2 2C5 12 0 7 0 2z" fill="#fff"/></svg><p>+1 (555) 010-0000</p></div>
    <div class="contact-line"><svg width="12" height="10" viewBox="0 0 12 10"><rect width="12" height="10" fill="#fff"/><path d="M0 0l6 5 6-5" stroke="#e34197" fill="none"/></svg><p>info@hourmarkcommercial.example</p></div>
  </div>
</footer>
<div class="bottom-bar"><span>©2014 Hourmark Commercial, All Rights Reserved</span><span>Terms of Service | Privacy Policy</span></div>
</body>
</html>
```